Booth flyer

I am looking for a flyer to pass out either at a booth that is set up at an event or to place as a flyer on a car. Quikkon Vtx is an affordable light reaction training device that will fit everyone's budget and flexible enough for any imaginable use. Our website is Quikkonvtx.example and Instagram is Quikkon.Vtx

```html
<!DOCTYPE html>
<html lang="en">
<head>
<meta charset="utf-8">
<title>Quikkon Vtx – Reaction Light Training Flyer</title>
<link href="https://fonts.googleapis.com/css2?family=Rajdhani:wght@300;400;500;600;700&display=swap" rel="stylesheet">
<style>
  :root {
    --red: #e73541;
    --charcoal: #333336;
    --ink: #2b2b2e;
    --white: #ffffff;
    --blush: #f8c3ca;
    --muted: #c4c4c7;
    --paper: #ffffff;
  }
  * { margin: 0; padding: 0; box-sizing: border-box; }
  html, body { width: 846px; height: 1200px; overflow: hidden; background: var(--paper); }
  body { font-family: 'Rajdhani', sans-serif; color: var(--ink); }
  .flyer { position: relative; width: 846px; height: 1200px; background: var(--paper); overflow: hidden; }

  .brand {
    position: absolute; left: 50px; top: 38px;
    display: flex; align-items: center; gap: 10px;
    font-size: 42px; font-weight: 700; color: var(--ink); letter-spacing: 0.5px;
  }
  .brand-dot { width: 16px; height: 16px; border-radius: 50%; background: var(--red); }

  .header-info { position: absolute; right: 47px; top: 38px; text-align: right; }
  .header-title { font-size: 29px; font-weight: 600; letter-spacing: 1px; line-height: 30px; }
  .header-url { font-size: 25px; font-weight: 300; letter-spacing: 1px; line-height: 25px; }

  .hero-panel { position: absolute; left: 0; top: 131px; width: 423px; height: 469px; background: var(--red); }
  .headline {
    position: absolute; left: 49px; top: 75px;
    font-size: 60px; font-weight: 700; line-height: 45px; color: var(--white); letter-spacing: 0.5px;
  }
  .tagline {
    position: absolute; left: 49px; top: 280px;
    font-size: 27px; font-weight: 700; line-height: 25px; color: var(--blush); letter-spacing: 0.5px;
  }
  .subline {
    position: absolute; left: 49px; top: 351px;
    font-size: 21px; font-weight: 600; line-height: 21px; color: var(--white); letter-spacing: 0.5px;
  }

  .info-panel { position: absolute; left: 0; top: 600px; width: 423px; height: 469px; background: var(--charcoal); color: var(--white); }
  .info-heading { position: absolute; left: 47px; top: 78px; font-size: 25px; font-weight: 700; line-height: 24px; letter-spacing: 0.5px; }
  .info-body { position: absolute; left: 47px; top: 136px; width: 350px; font-size: 18.5px; font-weight: 400; line-height: 22px; }
  .info-body strong { font-weight: 700; }
  .benefits-heading { position: absolute; left: 47px; top: 296px; font-size: 25px; font-weight: 700; letter-spacing: 0.5px; }
  .benefits { position: absolute; top: 337px; left: 48px; right: 0; display: flex; }
  .benefit {
    border-left: 3px solid var(--white); padding-left: 6px;
    font-size: 17px; font-weight: 700; line-height: 15.5px; color: var(--muted); letter-spacing: 0.3px;
  }
  .benefit:nth-child(1) { width: 137px; }
  .benefit:nth-child(2) { width: 101px; }

  .athlete-photo {
    position: absolute; left: 423px; top: 131px; width: 423px; height: 938px;
    background: linear-gradient(180deg, #c9d2c9 0%, #8da27f 18%, #e8ecf2 34%, #dfe4ec 62%, #b8c9c2 78%, #8a6a6a 100%);
  }
  .product-photo {
    position: absolute; left: 512px; top: 818px; width: 246px; height: 280px;
    background: linear-gradient(180deg, #9a9a9c 0%, #5b5b5e 45%, #2a2a2c 100%);
    border-radius: 10px 10px 14px 14px;
  }

  .contact-bar {
    position: absolute; left: 48px; right: 48px; top: 1122px; height: 32px;
    display: flex; align-items: center; font-size: 19px; font-weight: 400; color: var(--ink);
  }
  .contact-item { display: flex; align-items: center; gap: 9px; }
  .contact-divider { width: 1px; height: 12px; background: #c8c8c8; margin: 0 auto; }
  .contact-icon { width: 22px; height: 24px; flex: none; }
</style>
</head>
<body>
<main class="flyer">
  <div class="brand"><span class="brand-dot"></span>Quikkon Vtx</div>

  <div class="header-info">
    <div class="header-title">REACTION LIGHT TRAINING</div>
    <div class="header-url">WWW.QUIKKONVTX.EXAMPLE</div>
  </div>

  <section class="hero-panel">
    <h1 class="headline">BRING YOUR<br>TRAINING<br>TO THE NEXT<br>LEVEL</h1>
    <p class="tagline">AFFORDABLE LIGHT REACTION<br>TRAINING DEVICE</p>
    <p class="subline">FLEXIBLE ENOUGH FOR ANY<br>IMAGINABLE USE</p>
  </section>

  <section class="info-panel">
    <h2 class="info-heading">UP YOUR GAME WITH<br>REACTION TRAINING LIGHTS</h2>
    <p class="info-body">An easy to use, multi-light training system <strong>perfect for improving your visual processing</strong> in combination with the appropriate athletic response. Our training lights are portable and can be arranged in any configuration.</p>
    <h2 class="benefits-heading">KEY BENEFITS</h2>
    <div class="benefits">
      <div class="benefit">IMPROVED<br>OVERALL<br>PERFORMANCE</div>
      <div class="benefit">IMPROVED<br>DECISION<br>MAKING</div>
      <div class="benefit">IMPROVED<br>VISUAL<br>RESPONSE</div>
    </div>
  </section>

  <div class="athlete-photo" role="img" aria-label="Athlete in a white long-sleeve training shirt holding a basketball on an outdoor court"></div>
  <div class="product-photo" role="img" aria-label="Three reaction training lights on tripods beside their black carrying case"></div>

  <footer class="contact-bar">
    <div class="contact-item">
      <svg class="contact-icon" viewBox="0 0 22 24" aria-hidden="true">
        <polygon points="11,0 22,6 22,18 11,24 0,18 0,6" fill="var(--red)"/>
        <path d="M11 6.5a4 4 0 0 1 4 4c0 3-4 7-4 7s-4-4-4-7a4 4 0 0 1 4-4z" fill="none" stroke="#fff" stroke-width="1.3"/>
        <circle cx="11" cy="10.5" r="1.4" fill="none" stroke="#fff" stroke-width="1.2"/>
      </svg>
      <span>Oakridge, California</span>
    </div>
    <span class="contact-divider"></span>
    <div class="contact-item">
      <svg class="contact-icon" viewBox="0 0 22 24" aria-hidden="true">
        <polygon points="11,0 22,6 22,18 11,24 0,18 0,6" fill="var(--red)"/>
        <path d="M7.5 7.5c1-.8 1.6-.6 2 .3l.6 1.4c.3.7-.1 1.1-.6 1.5.6 1.3 1.6 2.3 2.9 2.9.4-.5.8-.9 1.5-.6l1.4.6c.9.4 1.1 1 .3 2-1 1.2-3 .8-5.1-1.2-2-2-2.5-4-1-5z" fill="none" stroke="#fff" stroke-width="1.2"/>
      </svg>
      <span>Tel: (555) 014-2280</span>
    </div>
    <span class="contact-divider"></span>
    <div class="contact-item">
      <svg class="contact-icon" viewBox="0 0 22 24" aria-hidden="true">
        <polygon points="11,0 22,6 22,18 11,24 0,18 0,6" fill="var(--red)"/>
        <rect x="5.5" y="8" width="11" height="8" fill="none" stroke="#fff" stroke-width="1.2"/>
        <polyline points="5.5,8 11,12.5 16.5,8" fill="none" stroke="#fff" stroke-width="1.2"/>
      </svg>
      <span>mail@quikkonvtx.example</span>
    </div>
  </footer>
</main>
</body>
</html>
```